Fernhollow Services

After a high quality design website. we are a company that provides services to people that own land and need a hand getting on top of the delayed jobs.
would want a number of tab/ pages for the web page.
Home page / About us page / services page / Gallery page. / Contact us page
we offer a wide range of services .listed below

Stock Work (title)

Stock movement
Break feeding
Temporary staffing

Spraying (title)

Spraying weeds
Spraying gorse

Pastures (title)

Fertilizing
Topping

Building (title)

Habitable sheds
Farm sheds
Sheep yards
Cattle yards
Repair farm buildings
Decks
Retaining walls

Fencing (title)

Stock fencing
Post & rail
Stock yards repair
Electric fencing install & repairs

Water Management (title)

Water trough installation
Water scheme install
Water trough cleaning
Farm water maintenance
Water ponds
Ornamental ponds
Drainage

General (title)

Lawn mowing
Hedge trimming
Pruning trees
Metaling drive ways & races
Water blasting
Small digger work
Little tip truck cartage
Home kill management
Mulching gorse
Section clearing

```html
<!DOCTYPE html>
<html lang="en">
<head>
<meta charset="utf-8">
<title>Fernhollow Services</title>
<link rel="stylesheet" href="https://fonts.googleapis.com/css2?family=Montserrat:wght@400;500;600;700&display=swap">
<style>
:root{
  --green:#7aa83a;
  --green-dark:#5e8a26;
  --ink:#111111;
  --muted:#8a8a8a;
  --dark:#0b0b0b;
  --white:#ffffff;
  --line:#d6d6d6;
}
*{box-sizing:border-box;margin:0;padding:0}
html,body{width:1200px;height:3861px;overflow:hidden;background:var(--white);font-family:'Montserrat',sans-serif;color:var(--ink)}
.page{position:relative;width:1200px;height:3861px;overflow:hidden}
.abs{position:absolute}
.brand{display:flex;align-items:center;gap:10px;font-weight:700;font-size:22px;color:var(--green)}
.brand .dot{width:30px;height:30px;border:3px solid var(--green);border-radius:50%}
.nav{position:absolute;top:48px;left:420px;display:flex;gap:26px;font-size:13px;color:#555;letter-spacing:.3px}
.nav .active{color:var(--green);position:relative}
.nav .active:before{content:"";position:absolute;left:-12px;right:-12px;top:-48px;height:6px;background:var(--green)}
.call{position:absolute;left:913px;top:36px;display:flex;gap:10px;align-items:center}
.call .icon{width:40px;height:40px;border-radius:6px;background:var(--green);display:flex;align-items:center;justify-content:center}
.call small{display:block;font-size:11px;color:#333}
.call b{font-size:16px;color:var(--green)}
.hero-photo{position:absolute;left:0;top:114px;width:1200px;height:670px;background:linear-gradient(120deg,#8a5a45 0%,#d9a58e 35%,#e9c3b0 55%,#c98c6e 80%,#7b4d38 100%)}
.hero-card{position:absolute;left:92px;top:215px;width:508px;height:315px;background:rgba(255,255,255,.9);border-bottom-right-radius:200px;padding:40px 20px}
.hero-card .kicker{font-size:17px;font-weight:500}
.hero-card h1{font-size:78px;color:var(--green);font-weight:600;line-height:1;margin-top:8px}
.hero-card p{font-size:14px;line-height:29px;margin-top:18px;color:#333}
.btn{display:inline-flex;align-items:center;justify-content:space-between;gap:20px;background:var(--green);color:var(--white);border-radius:26px;font-size:15px;padding:0 28px 0 32px;height:50px;box-shadow:3px 4px 6px rgba(0,0,0,.2)}
.btn .arr{width:16px;height:16px;border-radius:50%;background:var(--white);display:flex;align-items:center;justify-content:center}
.dots{position:absolute;left:112px;top:564px;display:flex;gap:6px}
.dots span{width:14px;height:14px;border-radius:50%;background:#ddd}
.dots .on{background:var(--green);border:2px solid #fff}
.eyebrow{font-size:17px;color:#555}
.big{font-size:52px;font-weight:600;line-height:60px}
.big .g{color:var(--green)}
.under{background:linear-gradient(transparent 62%,var(--green) 62%,var(--green) 82%,transparent 82%)}
.body{font-size:15px;line-height:24px;color:var(--muted)}
.body.strong{color:#777;font-weight:500}
.card{position:absolute;top:1190px;width:224px}
.card .ph{height:266px;border-radius:3px}
.card span{display:block;margin-top:11px;font-size:19px;font-weight:600}
.gallery{position:absolute;left:112px;top:2494px;display:grid;grid-template-columns:repeat(4,233px);gap:15px 15px}
.gallery div{height:237px}
.footer-bg{position:absolute;left:0;top:3200px;width:1200px;height:661px}
.form{position:absolute;left:628px;top:3296px;width:461px;height:379px;background:var(--white);padding:40px 20px}
.form .f{border:1px solid var(--line);height:44px;margin-bottom:11px;font-size:14px;color:#666;padding:12px 14px}
.form .f.msg{height:78px}
.form .send{position:absolute;right:22px;bottom:28px;background:var(--green);color:#fff;font-size:14px;font-weight:600;padding:10px 20px;border-radius:18px}
.contact-item{position:absolute;left:113px;display:flex;gap:18px;color:#fff;font-size:16px;line-height:23px}
.social{position:absolute;left:117px;top:3614px;display:flex;gap:8px}
.social span{width:34px;height:34px;border:2px solid #fff;border-radius:50%}
.flinks{position:absolute;left:113px;top:3782px;font-size:13px;color:#fff;word-spacing:2px}
</style>
</head>
<body>
<div class="page">

<header>
  <div class="brand abs" style="left:95px;top:40px"><span class="dot"></span>Fernhollow Services</div>
  <nav class="nav"><span class="active">HOME</span><span>ABOUT US</span><span>SERVICES ▾</span><span>GALLERY</span><span>CONTACT US</span></nav>
  <div class="call">
    <div class="icon"><svg width="22" height="22" viewBox="0 0 24 24" fill="none" stroke="#fff" stroke-width="2"><path d="M4 14v-2a8 8 0 0 1 16 0v2"/><rect x="3" y="13" width="4" height="6" rx="1"/><rect x="17" y="13" width="4" height="6" rx="1"/></svg></div>
    <div><small>Have Any Questions</small><b>+1 555 010 4477</b></div>
  </div>
</header>

<section class="hero">
  <div class="hero-photo" role="img" aria-label="Bright room with moving boxes, plants and a window"></div>
  <svg class="abs" style="left:0;top:690px" width="1200" height="100" viewBox="0 0 1200 100" preserveAspectRatio="none">
    <path d="M0 20 C300 60 500 95 620 88 C800 78 1000 50 1200 30 L1200 100 L0 100Z" fill="#fff"/>
    <path d="M0 15 C250 40 450 80 620 80 C820 80 1000 45 1200 20 L1200 30 C1000 55 820 90 620 90 C450 92 250 65 0 45Z" fill="var(--green)"/>
  </svg>
  <div class="hero-card">
    <div class="kicker">Fernhollow Services</div>
    <h1>Stock Work</h1>
    <p>Lorem ipsum is placeholder text commonly used in the graphic, print, and publishing industries for previewing lay-outs and visual mockups.</p>
  </div>
  <div class="btn abs" style="left:112px;top:480px;width:202px">Learn More <span class="arr"><svg width="9" height="9" viewBox="0 0 10 10"><path d="M3 2l4 3-4 3" stroke="var(--green)" stroke-width="2" fill="none"/></svg></span></div>
  <div class="dots"><span></span><span></span><span class="on"></span><span></span><span></span></div>
</section>

<section class="services">
  <div class="eyebrow abs" style="left:112px;top:874px">Our Services</div>
  <h2 class="big abs" style="left:112px;top:903px">We Offer<br>A <span class="g">Wide Range</span><br><span class="under">Of Services.</span></h2>
  <p class="body abs" style="left:597px;top:884px;width:500px">Lorem ipsum dolor sit amet, consectetur adipiscing elit, sed aliqua. Ut enim ad minim veniam, quis nostrud ex ea commodo consequat.</p>
  <p class="body strong abs" style="left:597px;top:980px;width:500px">Duis aute irure dolor in reprehenderit in voluptate velit esse cillum dolore eu fugiat nulla pariatur.</p>
  <div class="btn abs" style="left:596px;top:1064px;width:200px">Contact Us <span class="arr"><svg width="9" height="9" viewBox="0 0 10 10"><path d="M3 2l4 3-4 3" stroke="var(--green)" stroke-width="2" fill="none"/></svg></span></div>
  <div class="abs" style="left:1060px;top:1098px;width:28px;height:28px;background:var(--green-dark);display:flex;align-items:center;justify-content:center"><svg width="12" height="12" viewBox="0 0 10 10"><path d="M3 1l4 4-4 4" stroke="#fff" stroke-width="2" fill="none"/></svg></div>
  <svg class="abs" style="left:1066px;top:1142px" width="16" height="16" viewBox="0 0 10 10"><path d="M7 1L3 5l4 4" stroke="#777" stroke-width="2" fill="none"/></svg>

  <div class="card" style="left:-99px"><div class="ph" role="img" aria-label="Worker with ladder in a room" style="background:linear-gradient(#6b5a45,#c9a27d)"></div><span style="text-align:right">k</span></div>
  <div class="card" style="left:135px"><div class="ph" role="img" aria-label="Worker spraying weeds" style="background:linear-gradient(#3d6b2f,#7e9b5a)"></div><span>Spraying</span></div>
  <div class="card" style="left:370px"><div class="ph" role="img" aria-label="Green pasture under blue sky" style="background:linear-gradient(#9cc3e8 0%,#cfe1ef 45%,#6c9a3a 60%,#4f7f2a)"></div><span>Pastures</span></div>
  <div class="card" style="left:605px"><div class="ph" role="img" aria-label="Small farm shed building" style="background:linear-gradient(#e8ecef 0%,#bcc4c9 40%,#7a8a93 60%,#6f8a4a)"></div><span>Building</span></div>
  <div class="card" style="left:840px"><div class="ph" role="img" aria-label="Wooden fence and lawn" style="background:linear-gradient(#dfe9f0 0%,#5f8b3a 35%,#9a6a44 55%,#6fa23c)"></div><span>Fencing</span></div>
  <div class="card" style="left:1075px"><div class="ph" role="img" aria-label="Worker checking water pipes" style="background:linear-gradient(135deg,#9ab2c6,#d77a3a 50%,#4b6781)"></div><span style="white-space:nowrap">Water Management</span></div>
</section>

<section class="about">
  <div class="abs" role="img" aria-label="Collage of a customer, a worker, a lawn mower and a tradesman taking notes" style="left:111px;top:1655px;width:460px;height:575px">
    <div class="abs" style="left:0;top:0;width:250px;height:270px;border-top-left-radius:250px;background:linear-gradient(135deg,#d9c7b3,#b98a6d)"></div>
    <div class="abs" style="left:250px;top:0;width:165px;height:270px;background:linear-gradient(#ededed,#2d3a4a)"></div>
    <div class="abs" style="left:0;top:305px;width:250px;height:270px;border-bottom-right-radius:250px;background:linear-gradient(#2e4a22,#5fa52f)"></div>
    <div class="abs" style="left:250px;top:200px;width:210px;height:350px;border-radius:105px;border:6px solid #fff;background:linear-gradient(#3f5a78,#c1863a)"></div>
  </div>
  <div class="eyebrow abs" style="left:600px;top:1660px">About Us</div>
  <h2 class="big abs" style="left:600px;top:1690px">Lorem used<br>in a <span class="g">consectetur</span><br><span class="under">Of Services.</span></h2>
  <p class="body abs" style="left:600px;top:1886px;width:500px">Lorem ipsum dolor sit amet, consectetur adipiscing elit, sed aliqua. Ut enim ad minim veniam, quis nostrud ex ea commodo consequat.</p>
  <p class="body strong abs" style="left:600px;top:1982px;width:500px">Duis aute irure dolor in reprehenderit in voluptate velit esse cillum dolore eu fugiat nulla pariatur.</p>
  <p class="body abs" style="left:600px;top:2054px;width:490px">Aute irure dolor in reprehenderit in voluptate velit esse cillum dolore eu fugiat nulla pariatur. Excepteur sint occaecat cupi-datat non proident, sunt in culpa qui officia deserunt mollit anim id est laborum.</p>
  <div class="btn abs" style="left:600px;top:2180px;width:202px">Learn More <span class="arr"><svg width="9" height="9" viewBox="0 0 10 10"><path d="M3 2l4 3-4 3" stroke="var(--green)" stroke-width="2" fill="none"/></svg></span></div>
</section>

<section>
  <h2 class="big abs" style="left:0;width:1200px;text-align:center;top:2386px"><span class="under">Our Gallery</span></h2>
  <div class="gallery">
    <div role="img" aria-label="Rolling farmland at sunrise" style="background:linear-gradient(#d7dde0,#a8b08a 55%,#6f8a3a)"></div>
    <div role="img" aria-label="Worker in hard hat on radio" style="background:linear-gradient(135deg,#c9d4dc,#d9772e 55%,#3f4a55)"></div>
    <div role="img" aria-label="Wooden fence with shrubs" style="background:linear-gradient(#d9e4ec,#6a8f3a 30%,#8a5d3c 55%,#5f9a30)"></div>
    <div role="img" aria-label="Worker opening a drain cover" style="background:linear-gradient(135deg,#b7a39a,#2c3f6a 55%,#9a7e72)"></div>
    <div role="img" aria-label="Gardener spraying plants" style="background:linear-gradient(135deg,#c9c48a,#4f7a3a 60%,#3a5a8a)"></div>
    <div role="img" aria-label="Person carrying moving boxes" style="background:linear-gradient(135deg,#f4c27a,#c98a52 50%,#6a4a32)"></div>
    <div role="img" aria-label="Drainage pipe laid in soil" style="background:linear-gradient(135deg,#8a7e6c,#c9c3b8 50%,#5a5f66)"></div>
    <div role="img" aria-label="Technician in hard hat at work" style="background:linear-gradient(135deg,#9aa3aa,#d86a20 50%,#2d3238)"></div>
  </div>
  <div class="btn abs" style="left:499px;top:3037px;width:203px">View More <span class="arr"><svg width="9" height="9" viewBox="0 0 10 10"><path d="M3 2l4 3-4 3" stroke="var(--green)" stroke-width="2" fill="none"/></svg></span></div>
</section>

<footer>
  <svg class="footer-bg" width="1200" height="661" viewBox="0 0 1200 661" preserveAspectRatio="none">
    <path d="M0 80 C300 10 550 0 700 8 C900 20 1080 40 1200 60 L1200 661 L0 661Z" fill="var(--green)"/>
    <path d="M0 80 C300 25 550 20 700 28 C900 40 1080 65 1200 90 L1200 661 L0 661Z" fill="var(--dark)"/>
  </svg>
  <div class="abs" style="left:113px;top:3290px;color:#fff;font-size:17px">Contact Us</div>
  <div class="abs" style="left:113px;top:3316px;color:var(--green);font-size:38px;font-weight:500;border-bottom:2px solid var(--green);width:443px;padding-bottom:6px">Fernhollow Services</div>
  <div class="contact-item" style="top:3393px"><svg width="18" height="22" viewBox="0 0 24 30"><path d="M12 0a10 10 0 0 0-10 10c0 8 10 20 10 20s10-12 10-20A10 10 0 0 0 12 0z" fill="var(--green)"/><circle cx="12" cy="10" r="4" fill="var(--dark)"/></svg><div>88 Kowhai Lane,<br>Millbrook Valley,<br>40217</div></div>
  <div class="contact-item" style="top:3481px"><svg width="18" height="18" viewBox="0 0 24 24"><path d="M6 2l4 4-2 3c1 3 4 6 7 7l3-2 4 4-3 4C10 22 2 14 2 5z" fill="var(--green)"/></svg><div>Phone:<br>+1 555 010 4477</div></div>
  <div class="contact-item" style="top:3544px"><svg width="18" height="14" viewBox="0 0 24 18"><rect width="24" height="18" fill="var(--green)"/><path d="M0 0l12 9 12-9" stroke="var(--dark)" stroke-width="2" fill="none"/></svg><div>Email:<br>info@fernhollowservices.com</div></div>
  <div class="social"><span></span><span></span><span></span></div>

  <div class="form">
    <div class="f">Name</div>
    <div class="f">Phone</div>
    <div class="f">Email</div>
    <div class="f msg">Message Here</div>
    <div class="send">Get Started Now!</div>
  </div>

  <div class="abs" style="left:113px;top:3729px;width:976px;height:1px;background:#444"></div>
  <div class="flinks">Home &nbsp;| &nbsp; About Us &nbsp;| &nbsp; Services &nbsp;| &nbsp; Gallery &nbsp;| &nbsp; Contact Us</div>
  <div class="brand abs" style="left:580px;top:3772px;font-size:22px"><span class="dot"></span>Fernhollow Services</div>
  <div class="abs" style="left:880px;top:3778px;width:209px;text-align:right;color:#fff;font-size:13px;line-height:19px">Fernhollow Services © 2024.<br>All Rights Reserved.</div>
</footer>

</div>
</body>
</html>
```